Letterhead Design Project

Attached is our new Logo and a copy of our old letter head
Looking to rebrand with our new logo

Reason: I want to show a business card design

Industry/Entity Type

Film Production

Colors

Requirements
Must have
• The information on the old letterhead

```html
<!DOCTYPE html>
<html lang="en">
<head>
<meta charset="utf-8">
<title>Norvane International – Letterhead</title>
<link href="https://fonts.googleapis.com/css2?family=Arimo:wght@400;700&display=swap" rel="stylesheet">
<style>
  :root {
    --bg: #e4e4e4;
    --paper: #fbfbfa;
    --brand-blue: #1c7bb0;
    --deep-blue: #0e4f74;
    --mid-blue: #1b6a94;
    --sky-blue: #2b9fd6;
    --orange: #e8641c;
    --orange-light: #f39a2e;
    --ink: #4a4a4a;
    --ink-soft: #7a7a7a;
    --white: #ffffff;
  }
  * { box-sizing: border-box; margin: 0; padding: 0; }
  html, body { width: 1200px; height: 720px; overflow: hidden; }
  body {
    background: var(--bg);
    font-family: "Arimo", Arial, sans-serif;
    color: var(--ink);
    position: relative;
  }
  .sheet {
    position: absolute;
    top: 49px;
    width: 440px;
    height: 622px;
    box-shadow: 0 2px 10px rgba(0,0,0,.12);
    overflow: hidden;
  }
  /* Reverse side */
  .sheet--reverse {
    left: 130px;
    display: flex;
    align-items: center;
    justify-content: center;
  }
  .reverse-texture {
    position: absolute; inset: 0;
    background: radial-gradient(ellipse at 50% 40%, var(--mid-blue) 0%, var(--deep-blue) 85%);
  }
  .reverse-brand {
    position: relative;
    display: flex; align-items: center; gap: 10px;
    color: var(--white);
    font-weight: 700;
    font-size: 22px;
    letter-spacing: 3px;
    text-transform: uppercase;
  }
  .brand-dot {
    width: 12px; height: 12px; border-radius: 50%;
    background: var(--orange);
    flex: none;
  }
  /* Letter side */
  .sheet--letter {
    left: 630px;
    background: var(--paper);
    padding: 30px 34px 0 34px;
    font-size: 6.4px;
    line-height: 1.45;
  }
  .letter-header {
    display: flex; justify-content: space-between; align-items: flex-start;
  }
  .brand {
    display: flex; align-items: center; gap: 6px;
    color: var(--brand-blue);
    font-weight: 700;
    font-size: 12px;
    letter-spacing: 1.5px;
    text-transform: uppercase;
  }
  .brand .brand-dot { width: 8px; height: 8px; }
  .tagline {
    margin-top: 4px;
    font-size: 6px;
    color: var(--brand-blue);
  }
  .contact-list { list-style: none; font-size: 5.6px; color: var(--ink-soft); }
  .contact-list li { display: flex; align-items: center; gap: 4px; line-height: 1.6; }
  .contact-icon { width: 6px; height: 6px; flex: none; }
  .recipient { margin-top: 22px; }
  .letter-body p { margin-top: 9px; text-align: justify; }
  .letter-body .first { margin-top: 14px; }
  .closing { margin-top: 14px; }
  .signature { margin-top: 12px; }
  .letter-footer {
    position: absolute; left: 34px; right: 34px; top: 530px;
    font-size: 5px; color: var(--ink-soft);
  }
  .letter-footer strong { color: var(--ink); }
  .division-mark { color: var(--orange); }
  .footer-wave {
    position: absolute; left: 0; bottom: 0; width: 440px; height: 90px;
  }
</style>
</head>
<body>

<section class="sheet sheet--reverse" aria-label="Letterhead reverse side">
  <div class="reverse-texture" role="img" aria-label="Deep blue background with a faint wave pattern"></div>
  <div class="reverse-brand"><span class="brand-dot"></span>Norvane International</div>
</section>

<article class="sheet sheet--letter" aria-label="Letterhead front">
  <header class="letter-header">
    <div>
      <div class="brand"><span class="brand-dot"></span>Norvane International</div>
      <div class="tagline">Supply &amp; Management of Infrastructure &amp; Logistics</div>
    </div>
    <ul class="contact-list">
      <li><svg class="contact-icon" viewBox="0 0 10 10"><circle cx="5" cy="5" r="4" fill="var(--sky-blue)"/></svg>0400 123 456</li>
      <li><svg class="contact-icon" viewBox="0 0 10 10"><circle cx="5" cy="5" r="4" fill="var(--sky-blue)"/></svg>hello@norvane.example</li>
      <li><svg class="contact-icon" viewBox="0 0 10 10"><circle cx="5" cy="5" r="4" fill="var(--sky-blue)"/></svg>www.norvane.example</li>
      <li><svg class="contact-icon" viewBox="0 0 10 10"><circle cx="5" cy="5" r="4" fill="var(--sky-blue)"/></svg>PO Box 12 Harbour City 4000</li>
    </ul>
  </header>

  <address class="recipient" style="font-style:normal">
    Ms. Ada Lane<br>Managing Director<br>Company Name<br>100 Harbour Street<br>City
  </address>

  <div class="letter-body">
    <p class="first">Lorem ipsum dolor sit amet, consectetur adipiscing elit. Nam rutrum, mauris ut mi, facilisis nisl orci, egestas ut, fermentum at, tellus. Duis tincidunt lectus quis dui viverra vestibulum. Suspendisse vulputate aliquam dui. Nulla elementum dui ut augue.</p>
    <p>Aliquam vehicula mi at mauris. Maecenas placerat, nisl at consequat rhoncus, sem nunc gravida justo, quis eleifend arcu velit quis lacus. Morbi magna magna, tincidunt a, mattis non, imperdiet vitae, tellus.</p>
    <p>Mauris eget eros. Pellentesque habitant morbi tristique senectus et netus et malesuada fames ac turpis egestas. In pretium felis non lectus. Nullam sed justo vel dolor iaculis cursus.</p>
    <p>Mauris nunc quam, venenatis nec, euismod sit amet, egestas placerat, est. Cras velit. Donec convallis porta sapien, vitae semper lorem tempor eget. Duis quam. Nam eget nunc.</p>
    <p class="closing">Thank you for being one of our valued customers.</p>
    <p class="signature">Name Here<br>CEO</p>
  </div>

  <footer class="letter-footer">
    <strong>Norvane International Pty Ltd are divisions of:</strong><br>
    <span class="division-mark">•</span> Norvane Film Services &nbsp;|&nbsp; Norvane Film Escorts &nbsp;|&nbsp; Norvane Tour Management &nbsp;|&nbsp; Norvane Driver<br>
    ACN 000 000 000 ABN 00 000 000 000
  </footer>

  <svg class="footer-wave" viewBox="0 0 440 90" preserveAspectRatio="none" aria-hidden="true">
    <defs>
      <linearGradient id="waveOrange" x1="0" x2="1">
        <stop offset="0" stop-color="var(--orange)"/>
        <stop offset="1" stop-color="var(--orange-light)"/>
      </linearGradient>
      <linearGradient id="waveBlue" x1="0" x2="1">
        <stop offset="0" stop-color="var(--deep-blue)"/>
        <stop offset="1" stop-color="var(--sky-blue)"/>
      </linearGradient>
    </defs>
    <path d="M0 20 C120 50 300 60 440 30 L440 90 L0 90 Z" fill="url(#waveBlue)"/>
    <path d="M0 30 C130 62 300 72 440 48 L440 90 L0 90 Z" fill="url(#waveOrange)"/>
    <path d="M0 52 C140 78 300 84 440 70 L440 90 L0 90 Z" fill="var(--orange)"/>
  </svg>
</article>

</body>
</html>
```